Research Program Web Site

Goal:
-Create photoshop or HTML+CSS mockup of homepage for the Program for Knowledge Systems .
- Also create a child page which would be used to frame more detailed information - e.g. a list of publications, blog page, project activities, staff page.
Details:
The homepage is intended to convey:
- The mission of the program
- Link to overviews of research projects, preferably with brief teaser descriptions
- Display information on upcoming events, publications and tweets
- Show a connection to Varnholt and the Varnholt libraries
- Encourage viewers to follow/share content via social studio
Target audience:
- Research funders interested in an overview of the program, its major research areas, and research outputs (such as program publications and software, awards)
- Varnholt community (faculty, library staff, and students) interested in current information (blogs/tweets), events, and possible collaboration opportunities
Hosting:
- The site will eventually be hosted on datacraft.varnholt.example using a CMS (Drupal)
- There will be opportunity for further website implementation work if desired
Existing material:
- A text overview of the research program is included in the appendix attached to this document
- Much of the information on research projects is currently described here: http://drjbrenner.blogspot.example/dr-brenners-ongoing-studies-and-work-aka-what-is-joel-up-to/ This content will be moved to the program site when completed.
Themes:
- Varnholt color scheme is here, it is not required, but could be used for inspiration: http://web.varnholt.example/visualstyle/palette/index.html
- Varnholt libraries home page is here: http://libraries.varnholt.example/.
- The program page should borrow some design element from the library page if possible, and include the library and Varnholt logos somewhere on the page - but not as the most prominent branding element.
- Overall look and feel should be professional and serious, but modern
Comparison sites:
For comparison here are several pages for similar sites that are done fairly well:
http://www.orlandsurvey.example/
http://www.studio.varnholt.example/
http://www.dq.kestrelford.example/
- The orland and studio sites have the cleanest design.
- Both orland and dq are successful in conveying information about upcoming evevnts, publication and tweets
- Studio lab shows the right connection to larger organization
- Orland site communicates better the mission of the organization
Updates
A number of you have noted that the program description attachment was missing. I have now uploaded it. Thanks much - Joel
Thanks to those who have submitted designs so far. I have noticed that none of the designs thus far submitted include all of the elements requested in the design brief (task description). For clarification, I will emphasize these required elements:
- an area to describe the mission of the program
4. Branding/theming
Reason: Provide additional time for review of designs by colleagues on this end
Thanks,
Joel
Target Market(s)
- Research funders interested in an overview of the program, its major research areas, and research outputs (such as program publications and software
Industry/Entity Type
Library
Requirements
Nice to have
- hemes:
Comparison sites:
http://www.studio.varnholt.example/

```html
<!DOCTYPE html>
<html lang="en">
<head>
<meta charset="utf-8">
<title>Varnholt Information Science</title>
<link rel="stylesheet" href="https://fonts.googleapis.com/css2?family=Arimo:ital,wght@0,400;0,700;1,400&display=swap">
<style>
:root{
  --page:#dcdcdc;
  --panel:#ffffff;
  --slate:#666666;
  --nav:#6e6e6e;
  --link:#a31f1f;
  --accent:#c8262f;
  --rule:#cfcfcf;
  --ink:#111111;
  --caption:rgba(90,90,90,.82);
  --search:#b3b3b3;
}
*{box-sizing:border-box;margin:0;padding:0}
html,body{width:1060px;height:1200px;overflow:hidden;background:var(--page);font-family:"Arimo",Arial,sans-serif;color:var(--ink)}
a{color:inherit;text-decoration:none}
ul{list-style:none}
.canvas{position:relative;width:1060px;height:1200px}

.brand{position:absolute;left:0;width:1060px;top:18px;text-align:center;font-size:36px;color:#666;letter-spacing:-1px;line-height:40px}

.main-nav{position:absolute;top:84px;left:106px;font-size:14px;font-weight:700;color:var(--nav);letter-spacing:.3px}
.main-nav a{position:absolute;white-space:nowrap}
.search{position:absolute;left:799px;top:76px;width:155px;height:25px;background:var(--search)}
.search svg{position:absolute;right:6px;top:5px}

.backdrop{position:absolute;left:698px;top:140px;width:256px;height:1024px;background:var(--slate)}
.footer-band{position:absolute;left:172px;top:1000px;width:782px;height:164px;background:var(--slate);color:#fff;font-size:11px}
.footer-links{position:absolute;left:19px;top:53px;white-space:nowrap}
.footer-links span{margin:0 4px}
.footer-contact{position:absolute;left:19px;top:86px;line-height:16px}
.copyright{position:absolute;right:106px;top:1176px;font-size:10px;color:#555}

.content{position:absolute;left:106px;top:118px;width:592px;height:902px;background:var(--panel);box-shadow:2px 2px 4px rgba(0,0,0,.35)}
.hero{position:absolute;left:4px;top:5px;width:583px;height:318px;background:linear-gradient(120deg,#3d3a34 0%,#5b4a3c 30%,#c89a72 55%,#a56d63 75%,#6f5a4c 100%)}
.hero-caption{position:absolute;left:0;bottom:0;width:100%;height:44px;background:var(--caption);color:#fff;font-size:20px;line-height:44px;padding-left:13px}
.hero-dots{position:absolute;right:13px;top:20px;display:flex;gap:3px}
.hero-dots i{width:7px;height:6px;background:#bbb}
.hero-dots i.on{background:var(--accent)}

.block{position:absolute;width:262px}
.block h2{font-size:13.5px;font-weight:700;height:27px;line-height:16px;border-bottom:1px solid var(--rule)}
.block li{font-size:11px;line-height:14px;color:var(--link);padding:5.5px 0;border-bottom:1px solid var(--rule)}
.block li em{font-style:italic}
.more{display:block;text-align:right;font-size:11px;color:var(--ink);padding-top:5px}
.more::after{content:"";display:inline-block;margin-left:2px;border:4px solid transparent;border-top:5px solid var(--ink);border-bottom:0;vertical-align:1px}
.col-a{left:17px}
.col-b{left:314px}
.row-1{top:356px}
.row-2{top:628px}

.sidebar{position:absolute;left:715px;top:168px;width:225px;color:#fff}
.sidebar h1{font-size:19.5px;font-weight:700;line-height:24px}
.mission{font-size:11.5px;line-height:16.4px;margin-top:7px}
.learn{display:block;text-align:right;font-size:10px;font-weight:700;font-style:italic;color:var(--accent);margin-top:8px}
.side-head{position:absolute;left:715px;width:221px;border-top:2px solid #d9d9d9;border-bottom:2px solid #d9d9d9;color:#ddd;font-size:12.5px;font-weight:700;height:27px;line-height:23px}
.tweets{position:absolute;left:715px;top:518px;width:221px}
.tweet{position:relative;background:#fff;color:#222;font-size:10.5px;line-height:14px;padding:10px 9px;height:79px;margin-bottom:13px}
.tweet::after{content:"";position:absolute;right:14px;bottom:-7px;border-left:6px solid transparent;border-top:7px solid #fff}
.tweet small{font-size:8px;font-style:italic;text-decoration:underline;margin-left:4px}
.follow{position:absolute;left:771px;top:795px;width:165px;height:19px;background:#f3f3f3;border:1px solid #ccc;border-radius:3px;font-size:8.5px;color:#333;line-height:17px;padding-left:19px;white-space:nowrap;overflow:hidden}
.follow::before{content:"";position:absolute;left:5px;top:4px;width:9px;height:9px;border-radius:50%;background:#4aa8e0}
.social{position:absolute;left:715px;top:890px;display:flex;gap:4px}
.social span{width:27px;height:27px;border-radius:3px}
.share{position:absolute;left:715px;top:930px;width:111px;height:14px;background:#f4f4f4;border:1px solid #bbb;font-size:8px;line-height:12px;padding-left:18px;color:#333}
.share::before{content:"";position:absolute;left:3px;top:2px;width:8px;height:8px;background:#e25c2a}
.partner{position:absolute;top:960px;color:#fff;font-size:15px;line-height:20px}
</style>
</head>
<body>
<div class="canvas">
  <div class="brand">Varnholt Information Science</div>

  <nav class="main-nav">
    <a href="#" style="left:0">ABOUT</a>
    <a href="#" style="left:83px">RESEARCH</a>
    <a href="#" style="left:193px">PEOPLE</a>
    <a href="#" style="left:284px">EVENTS</a>
    <a href="#" style="left:373px">NEWS</a>
    <a href="#" style="left:448px">ADMISSIONS</a>
    <a href="#" style="left:569px">SPONSORSHIP</a>
  </nav>
  <div class="search">
    <svg width="15" height="15" viewBox="0 0 15 15"><circle cx="6" cy="6" r="4.3" fill="none" stroke="#666" stroke-width="2"/><line x1="9.2" y1="9.2" x2="13.5" y2="13.5" stroke="#666" stroke-width="2.6"/></svg>
  </div>

  <div class="backdrop"></div>
  <footer class="footer-band">
    <div class="footer-links">Home<span>|</span>About<span>|</span>Research<span>|</span>People<span>|</span>Events<span>|</span>News<span>|</span>Admissions<span>|</span>Sponsorship</div>
    <div class="footer-contact">48 Harrow Quay, Varnholt, MA 02190<br>Tel: +1 555-014-2277<br>Email: info@knowledgesystems.varnholt.example</div>
  </footer>
  <div class="copyright">©2013 Varnholt Information Science. All Rights Reserved.</div>

  <main class="content">
    <div class="hero" role="img" aria-label="Photo of a smiling student beside a computer in a library">
      <div class="hero-caption">Lorem Ipsum Dolor Sit Amet Consectetur Adiping
        <div class="hero-dots"><i class="on"></i><i></i><i></i><i></i></div>
      </div>
    </div>

    <section class="block col-a row-1">
      <h2>Research Projects</h2>
      <ul>
        <li>Lorem ipsum dolor sit amet, conseetur adipiscing elit</li>
        <li>Morbi vitae tristique orci nunc quis dui quam, id iaculis dui praesent mollis vehicula nunc in gravida</li>
        <li>Fusce dictum consequat bibendum sed sed nisl nunc curabitur sit amet placerat justo</li>
        <li>Proin id vehicula enim donec ornare</li>
        <li>Tristique odio sit amet elementum in nisi consequat diam volutpat mollis quis in erat donec pellentesque</li>
        <li>Surpis et nisl luctus laoreet maecenas ac lorem sem</li>
      </ul>
      <a class="more" href="#">More</a>
    </section>

    <section class="block col-b row-1">
      <h2>Upcoming Events</h2>
      <ul>
        <li>Vivamus rhoncus pellentesque rhncus In hendrerit neque pellentes que ane <em>(Feb. 14, 2103)</em></li>
        <li>Ncidunt in eleifend erat gravida nulla quis eros id nun porta convallis &nbsp;<em>(Feb. 26, 2103)</em></li>
        <li>Quisque auctor consequat nibh &nbsp;<em>(March 5, 2103)</em></li>
        <li>Commodo laoreet nulla <em>(March 13, 2103)</em></li>
        <li>scelerisque tempus phasellus id urna ut sapieh kjjig consequantn &nbsp;<em>(March 30, 2103)</em></li>
        <li>Acinia rutrum non at augueac odnunc <em>(Apr. 8, 2103)</em></li>
      </ul>
      <a class="more" href="#">More</a>
    </section>

    <section class="block col-a row-2">
      <h2>Publications</h2>
      <ul>
        <li>Praesent quis ante orci, eu rutrum arcu aliquam a posuere turpis. Sed at ante quis ante convallis</li>
        <li>Raesent felis justo, iaculis id porttitor ac, dapibus nec nunc cum sociis natoque penatibus et magnis dis</li>
        <li>Aliquam odio dolor, sodales vel adipiscing rhoncus</li>
        <li>Sed quis orci non leo aliquet rutrum vel sit amet</li>
        <li>In hac habitasse platea dictumst: Sed molestie risus eget urna venenatis a pharetra tortor posuer</li>
        <li>Donec ac venenatis odio sed sit amet nibh dolorne</li>
      </ul>
      <a class="more" href="#">More</a>
    </section>

    <section class="block col-b row-2">
      <h2>Associations</h2>
      <ul>
        <li>Cras eu tellus lacus et tempus neque</li>
        <li>Morbi tincidunt blandit eros et consequat orci</li>
        <li>Suspendisse blandit arcu at risus feugiat et sodales nisl hendrerit nunc vitae risus nibh</li>
        <li>Morbi tincidunt laoreet metus, nec tristique felis consequat in. vestibulum ante ipsum primis in</li>
        <li>Curae; Sed massa sapien, venenatis ut ullamcorper non, sagittis in mauris</li>
        <li>Donec faucibus rhoncus tellus eget ullamcorper</li>
      </ul>
      <a class="more" href="#">More</a>
    </section>
  </main>

  <aside class="sidebar">
    <h1>Varnholt Information Science</h1>
    <p class="mission">Lorem ipsum dolor sit amet, consectetur adipiscing elit. Nam sed massa eget augue vehicula viverra ac eu odio. Maece posuere venenatis libero posuere adipisc. Maecenas laoreet viverra ligula vitae ullamcorper. Duis fermentum diam non erat aliquam euismod. Aliquam sollicitudin erat in erat auctor tristique. Praesent risus odio, facilisis adipiscing commodo nec, molestie id arcu. In fringilla laoreet dolor facilisis rhoncus. Pellentesque habitant morbi tristique senectus et netus esentto.</p>
    <a class="learn" href="#">→ LEARN MORE</a>
  </aside>

  <div class="side-head" style="top:478px">Recent Tweets</div>
  <div class="tweets">
    <div class="tweet">Lorem ipsum dolor sit amet, conse ctetur adipiscing elit. Nunc sed ante id urna rutrum interdum eget eget dui sollicitudin leo sit amet mauris. <small>2 days ago</small></div>
    <div class="tweet">Sed tempor, est quis adipiscing pulvinar, urna odio suscipit arcu, eget tincidunt est libero vitae nisi. Pellentesque habitant morbi tristique senectus netus. <small>3 days ago</small></div>
    <div class="tweet">Cras egestas interdum nibh volutp congu. Fusce nec lectus tortor, in facilisis felis. Kolu sce sollici tudin eleifend metus <small>5 days ago</small></div>
  </div>
  <a class="follow" href="#">Follow @Varnholt Information Science</a>

  <div class="side-head" style="top:849px">Connect with Us</div>
  <div class="social">
    <span style="background:#2d5aa8"></span>
    <span style="background:#3aa7e0"></span>
    <span style="background:#1f6aa8"></span>
    <span style="background:#2a4fa8"></span>
    <span style="background:#c8221e"></span>
    <span style="background:#ef7a22"></span>
  </div>
  <div class="share">SHARE</div>
  <div class="partner" style="left:715px">Varnholt Libraries</div>
  <div class="partner" style="left:850px">Varnholt</div>
</div>
</body>
</html>
```